Label or packaging Design for Hair Care Line

Dear Designer,
We are Corvella, a brand known for our premium hairstyling tools, and we are excited to expand into hair care. We are currently looking for a talented designer to create the label designs for our entire luxury hair care line.
This project is crucial in establishing our visual identity in the hair care market, and we aim to position ourselves alongside premium brands such as LTP, Dorvane Hair Atelier, and Pelmi.
Project Scope
We need a cohesive label design for our hair care line, which includes:
5 products (e.g., shampoo, conditioner, hair oil, styling cream, and a hair mask).
The designs should include:
Front label: Highlighting the product name, key features, and branding.
Our goal is to achieve a design that communicates premium luxury with a touch of professionalism. Below are the specific guidelines to help you align with our vision:
Style and Inspiration
Think of brands like LTP, Dorvane Hair Atelier, and Pelmi.
Luxury and Minimalism: Clean lines, sophisticated typography, and an elegant color palette.
Subtle femininity: premium finishes like metallic accents (gold, silver, or rose gold).
Brand Personality
Premium: Reflecting high quality and exclusivity.
Modern & Professional: Appealing to a refined, professional audience but also suitable for lifestyle-oriented customers.
Warm & Empowering: A brand that celebrates confidence and individuality.
Color Palette
Neutral tones like black, white, accented with metallics (gold or silver) for a luxurious feel.
Colors that feel timeless and elegant rather than trendy or overly bright.
Typography
Use clean, modern fonts (preferably sans-serif or serif for a refined look).
Clear and legible for all product details while maintaining a high-end aesthetic.
Materials and Finishes
Packaging Shape
The label designs should suit a variety of bottle and jar shapes (e.g., cylindrical, flat, or rounded).
Keep scalability in mind so the identity remains consistent across different products.
Deliverables
To understand the aesthetic we are aiming for, here are some brands to use as inspiration:
LTP: For its minimalistic and modern approach.
Dorvane Hair Atelier: For its combination of luxury and professional appeal.
Pelmi: For its soft femininity and lifestyle branding.
we would like to see your designs applied to a variety of packaging types to get an overall impression of how the brand identity works across different product formats. This includes:
A squeeze bottle (e.g., for styling creams or conditioners).
A glass bottle with a dropper (e.g., for a luxurious hair oil).
A shampoo/conditioner bottle (standard pump or flip-top cap).
A spray bottle (e.g., for leave-in treatments or heat protectors).
By creating designs for these different packaging types, we can better evaluate how cohesive and versatile the brand identity will be across the entire product line.

Updates
As you may have noticed from the designs, they don’t quite align with our briefing. The look needs to be clean and professional, similar to Dorvane, LTP, and the other examples we provided. Please address this, and we’ll check it!

Target Market(s)
europe and us
Font styles to use
Other font styles liked:
- century gothic

Look and feel
Each slider illustrates characteristics of the customer's brand and the style your logo design should communicate.

```html
<!DOCTYPE html>
<html lang="en">
<head>
<meta charset="utf-8">
<title>Corvella Revitalizing Shampoo – Front Label</title>
<link rel="stylesheet" href="https://fonts.googleapis.com/css2?family=Questrial&family=Didact+Gothic&display=swap">
<style>
  :root {
    --label-black: #0c0c0d;
    --label-charcoal: #1a1a1c;
    --text-white: #f4f4f4;
    --text-grey: #c9c9c9;
    --gold: #e0ad3c;
    --gold-light: #f6d27a;
    --gold-deep: #a8731c;
    --rule: #3a3a3c;
  }
  * { margin: 0; padding: 0; box-sizing: border-box; }
  html, body {
    width: 670px;
    height: 1200px;
    overflow: hidden;
    background: var(--label-black);
  }
  .label {
    position: relative;
    width: 670px;
    height: 1200px;
    background: radial-gradient(ellipse at 50% 40%, var(--label-charcoal) 0%, var(--label-black) 70%);
    font-family: "Questrial", "Century Gothic", sans-serif;
    color: var(--text-white);
    text-align: center;
  }
  .brand-name {
    position: absolute;
    top: 150px;
    left: 0;
    width: 100%;
    font-size: 96px;
    letter-spacing: 2px;
    color: var(--text-white);
    line-height: 1;
  }
  .product-line {
    position: absolute;
    top: 300px;
    left: 0;
    width: 100%;
    padding: 18px 0;
    border-top: 1px solid var(--rule);
    border-bottom: 1px solid var(--rule);
    font-size: 34px;
    letter-spacing: 14px;
    color: var(--text-grey);
    line-height: 1;
  }
  .product-name {
    position: absolute;
    top: 405px;
    left: 0;
    width: 100%;
    font-size: 122px;
    letter-spacing: 3px;
    line-height: 1;
    color: var(--gold);
  }
  .key-ingredients {
    position: absolute;
    top: 540px;
    left: 0;
    width: 100%;
    font-family: "Didact Gothic", "Century Gothic", sans-serif;
    font-size: 38px;
    color: var(--gold);
    line-height: 1;
  }
  .gold-wave {
    position: absolute;
    top: 600px;
    left: 0;
    width: 670px;
    height: 220px;
    background:
      radial-gradient(ellipse 60% 30% at 55% 55%, rgba(246, 210, 122, 0.55) 0%, rgba(224, 173, 60, 0.25) 45%, rgba(12, 12, 13, 0) 75%),
      linear-gradient(100deg, rgba(12,12,13,0) 0%, rgba(168,115,28,0.35) 35%, rgba(246,210,122,0.45) 55%, rgba(168,115,28,0.25) 75%, rgba(12,12,13,0) 100%);
    mask-image: linear-gradient(180deg, transparent 0%, #000 30%, #000 70%, transparent 100%);
  }
  .feature-icons {
    position: absolute;
    top: 880px;
    left: 0;
    width: 100%;
    display: flex;
    justify-content: center;
    gap: 60px;
  }
  .feature {
    width: 120px;
    display: flex;
    flex-direction: column;
    align-items: center;
  }
  .feature-badge {
    width: 66px;
    height: 66px;
  }
  .feature-text {
    margin-top: 10px;
    font-size: 16px;
    line-height: 1.15;
    color: var(--text-grey);
  }
  .net-weight {
    position: absolute;
    top: 1085px;
    left: 0;
    width: 100%;
    padding-top: 22px;
    border-top: 1px solid var(--rule);
    font-size: 32px;
    letter-spacing: 1px;
    color: var(--gold);
    line-height: 1;
  }
</style>
</head>
<body>
  <main class="label">
    <div class="brand-name">corvella</div>
    <div class="product-line">REVITALIZING</div>
    <h1 class="product-name">SHAMPOO</h1>
    <p class="key-ingredients">Ginseng &amp; Natural DHT</p>

    <div class="gold-wave" role="img" aria-label="Flowing gold silk ribbon decoration"></div>

    <ul class="feature-icons">
      <li class="feature">
        <svg class="feature-badge" viewBox="0 0 66 66" aria-hidden="true">
          <circle cx="33" cy="33" r="31" fill="none" stroke="var(--text-grey)" stroke-width="1.5"/>
          <rect x="29" y="15" width="8" height="6" fill="none" stroke="var(--text-grey)" stroke-width="1.5"/>
          <rect x="23" y="22" width="20" height="26" rx="4" fill="none" stroke="var(--text-grey)" stroke-width="1.5"/>
          <line x1="18" y1="18" x2="48" y2="48" stroke="var(--text-grey)" stroke-width="1.5"/>
        </svg>
        <span class="feature-text">Fragrance<br>free</span>
      </li>
      <li class="feature">
        <svg class="feature-badge" viewBox="0 0 66 66" aria-hidden="true">
          <circle cx="33" cy="33" r="31" fill="none" stroke="var(--text-grey)" stroke-width="1.5"/>
          <circle cx="33" cy="33" r="4" fill="var(--text-grey)"/>
          <ellipse cx="33" cy="33" rx="16" ry="7" fill="none" stroke="var(--text-grey)" stroke-width="1.5"/>
          <ellipse cx="33" cy="33" rx="16" ry="7" fill="none" stroke="var(--text-grey)" stroke-width="1.5" transform="rotate(60 33 33)"/>
          <ellipse cx="33" cy="33" rx="16" ry="7" fill="none" stroke="var(--text-grey)" stroke-width="1.5" transform="rotate(-60 33 33)"/>
        </svg>
        <span class="feature-text">Sulfate<br>Free</span>
      </li>
      <li class="feature">
        <svg class="feature-badge" viewBox="0 0 66 66" aria-hidden="true">
          <circle cx="33" cy="33" r="31" fill="none" stroke="var(--text-grey)" stroke-width="1.5"/>
          <path d="M40 16 L46 22 L32 38 L27 33 Z" fill="none" stroke="var(--text-grey)" stroke-width="1.5"/>
          <path d="M27 33 L32 38 C30 44 24 48 19 47 C21 43 21 37 27 33 Z" fill="none" stroke="var(--text-grey)" stroke-width="1.5"/>
          <line x1="18" y1="18" x2="48" y2="48" stroke="var(--text-grey)" stroke-width="1.5"/>
        </svg>
        <span class="feature-text">No artificial<br>colors</span>
      </li>
    </ul>

    <p class="net-weight">NET WT. 473ML (16OZ.)</p>
  </main>
</body>
</html>
```